Diabetes control iOS/Android app design

I need a modern app design with light colors that are easy on the eyes, This app is for diabetes control. Focusing on Sweet/carb control and its daily intake .. I have uploaded some wireframe pages to design . Light colors are preferred for design. I donot need too much Hussle and data on main page.
Name/title: Glucaro- Diabetes reversal

Target Market(s)

Diabetes patients

Industry/Entity Type

health

Colors
0094D4
00A9DD
6FCCEA
C7EBF8
E9F6FB
00AB8E
00BBA5
67D7C9
C6EFE9
E9F9F6
59FF00
82FF00
B8FF75
E3FFCB
F4FFEA
FFC000
F8CF3A
FAE287
FDF2CF
FEFAEE

Requirements
Should not have
• complicated design. It should be simple , modern and easy o eye.

```html
<!DOCTYPE html>
<html lang="en">
<head>
<meta charset="utf-8">
<title>Rehab app · Screens</title>
<link href="https://fonts.googleapis.com/css2?family=DM+Sans:wght@400;500;700&display=swap" rel="stylesheet">
<style>
:root{
  --page:#f2f2f2;
  --ink:#111;
  --muted:#555;
  --blue:#00A9DD;
  --blue-dark:#0a82c9;
  --blue-light:#6FCCEA;
  --blue-pale:#E9F6FB;
  --teal:#00AB8E;
  --green:#59FF00;
  --green-pale:#E3FFCB;
  --yellow:#FFC000;
  --red:#ff1a1a;
  --card:#fff;
  --screen:#f6f6f6;
  --line:#ececec;
}
*{margin:0;padding:0;box-sizing:border-box}
html,body{width:1095px;height:1200px;overflow:hidden;background:var(--page);font-family:'DM Sans',sans-serif;color:var(--ink)}
.stage{position:absolute;left:0;top:0;width:1839px;height:2016px;transform:scale(0.5955);transform-origin:0 0}
.headline{position:absolute;top:108px;width:100%;text-align:center;font-size:62px;font-weight:500;letter-spacing:-0.5px}
.subline{position:absolute;top:200px;width:100%;text-align:center;font-size:22px;color:#333}
.phone{position:absolute;width:312px;height:676px;background:var(--screen);overflow:hidden;box-shadow:0 16px 30px rgba(0,0,0,.12)}
.appbar{position:absolute;left:0;top:0;width:100%;height:62px;background:var(--blue);color:#fff}
.appbar .title{position:absolute;top:30px;width:100%;text-align:center;font-size:15px;font-weight:500}
.appbar .back{position:absolute;left:20px;top:31px}
.greeting{position:absolute;left:12px;top:25px;font-size:13px;font-weight:700}
.avatar{position:absolute;left:259px;top:15px;width:36px;height:36px;border-radius:50%;background:radial-gradient(circle at 50% 40%,#9a7a66,#5b4a42);border:2px solid #e3e3e3}
.card{position:absolute;left:16px;width:279px;background:var(--card);border-radius:3px;box-shadow:0 1px 3px rgba(0,0,0,.04)}
.card-title{position:absolute;width:100%;text-align:center;font-size:15px;font-weight:500}
.abs{position:absolute}
.tabs{position:absolute;left:15px;width:251px;height:27px;background:#eee;border-radius:3px;font-size:9px;color:#9a9a9a}
.tabs span{position:absolute;top:3px;width:81px;height:21px;line-height:21px;text-align:center}
.tabs .on{background:#fff;color:#222;border-radius:2px}
.nav{position:absolute;left:0;top:605px;width:100%;height:71px;background:#fff;border-top:1px solid var(--line)}
.home-bar{position:absolute;left:102px;top:61px;width:107px;height:4px;border-radius:2px;background:#bdbdbd}
.btn{position:absolute;left:15px;top:205px;width:281px;height:36px;background:var(--blue-dark);color:#fff;font-size:13px;text-align:center;line-height:36px;border-radius:2px}
.brand-name{position:absolute;left:0;top:115px;width:100%;text-align:center;font-size:28px;font-weight:500;color:var(--ink)}
.note{font-size:11px;color:#333;line-height:14px}
.step{position:absolute;left:13px;font-size:11px;color:#333}
.step b{display:inline-block;width:16px;height:16px;margin-right:8px;background:var(--green-pale);color:#333;font-weight:400;font-size:10px;text-align:center;line-height:16px}
.para{font-size:10.5px;color:#666;line-height:18px;white-space:nowrap}
.para a{color:var(--blue);text-decoration:underline}
svg text{font-family:'DM Sans',sans-serif}
</style>
</head>
<body>
<div class="stage">
  <h1 class="headline">High Fidelity Design</h1>
  <p class="subline">There might be some changes to be done in design. Please free feel to message me with changes</p>

  <!-- Home -->
  <section class="phone" style="left:332px;top:370px">
    <header class="appbar" style="height:59px">
      <span class="greeting">Hi Marcus</span>
      <div class="avatar" role="img" aria-label="User profile photo"></div>
    </header>
    <div class="card" style="top:78px;height:176px">
      <div class="card-title" style="top:19px">Sugar Count Today</div>
      <svg class="abs" style="left:0;top:0" width="279" height="176">
        <defs><linearGradient id="donutBlue" x1="0" y1="0" x2="0" y2="1"><stop offset="0" stop-color="#00A9DD"/><stop offset="1" stop-color="#6FCCEA"/></linearGradient></defs>
        <circle cx="139" cy="106" r="45" fill="none" stroke="#d9f1fa" stroke-width="9"/>
        <circle cx="139" cy="106" r="45" fill="none" stroke="url(#donutBlue)" stroke-width="9" stroke-dasharray="200 283" stroke-linecap="round" transform="rotate(-90 139 106)"/>
        <text x="139" y="112" text-anchor="middle" font-size="17" font-weight="500" fill="#00A9DD">15%</text>
      </svg>
    </div>
    <div class="card" style="top:268px;height:231px">
      <div class="card-title" style="top:16px">Consumption Today</div>
      <svg class="abs" style="left:0;top:0" width="279" height="231">
        <defs><linearGradient id="gaugeHot" x1="0" y1="0" x2="1" y2="0"><stop offset="0" stop-color="#FAE287"/><stop offset=".35" stop-color="#F8CF3A"/><stop offset=".65" stop-color="#ffa94d"/><stop offset="1" stop-color="#ff7b72"/></linearGradient>
        <linearGradient id="needleHot" x1="0" y1="1" x2="1" y2="0"><stop offset="0" stop-color="#ffb04d"/><stop offset="1" stop-color="#ff6a00"/></linearGradient></defs>
        <path d="M49.4 174 A90 90 0 1 1 228.6 174" fill="none" stroke="url(#gaugeHot)" stroke-width="5" stroke-linecap="round"/>
        <g stroke="#999" stroke-width="1">
          <line x1="56" y1="166" x2="62" y2="166"/><line x1="81" y1="108" x2="86" y2="113"/><line x1="139" y1="82" x2="139" y2="90"/><line x1="197" y1="108" x2="192" y2="113"/><line x1="222" y1="167" x2="216" y2="167"/>
        </g>
        <g font-size="8" fill="#999" text-anchor="middle">
          <text x="70" y="169">1</text><text x="93" y="124">2</text><text x="139" y="101">3</text><text x="185" y="124">4</text><text x="208" y="170">5</text>
        </g>
        <text x="139" y="65" text-anchor="middle" font-size="8" fill="#ff8c42">Fatal</text>
        <text x="52" y="199" text-anchor="middle" font-size="8" fill="#F8CF3A">Danger</text>
        <text x="225" y="199" text-anchor="middle" font-size="8" fill="#ff6b6b">Catastrophic</text>
        <polygon points="136,163 142,169 198,134" fill="url(#needleHot)"/>
        <circle cx="139" cy="166" r="7" fill="#fff" stroke="#e5e5e5"/>
        <text x="139" y="205" text-anchor="middle" font-size="14" fill="#111">5.6 <tspan font-size="6">mmol/L</tspan></text>
      </svg>
    </div>
    <nav class="nav">
      <svg class="abs" style="left:0;top:0" width="312" height="60" fill="none" stroke-width="1.6">
        <g stroke="#00A9DD" fill="#00A9DD"><circle cx="34" cy="27" r="4"/><circle cx="42" cy="27" r="4"/><path d="M27 38 q7-9 14 0z M35 38 q7-9 14 0z"/></g>
        <g stroke="#777"><rect x="91" y="25" width="12" height="14" rx="1"/><line x1="97" y1="25" x2="97" y2="39"/>
        <circle cx="156" cy="32" r="10"/><line x1="156" y1="27" x2="156" y2="37"/><line x1="151" y1="32" x2="161" y2="32"/>
        <rect x="206" y="26" width="16" height="5" rx="1"/><rect x="206" y="33" width="16" height="5" rx="1"/>
        <circle cx="273" cy="28" r="5"/><path d="M264 41 q9-11 18 0"/></g>
      </svg>
      <div class="home-bar"></div>
    </nav>
  </section>

  <!-- Rehab Monitor -->
  <section class="phone" style="left:764px;top:370px">
    <header class="appbar">
      <svg class="back" width="16" height="16" fill="none" stroke="#fff" stroke-width="1.6"><path d="M14 8H2M7 3L2 8l5 5"/></svg>
      <div class="title">Rehab Monitor</div>
    </header>
    <div class="card" style="top:82px;height:308px">
      <div class="card-title" style="top:18px">Daily Sugar Graph</div>
      <div class="tabs" style="top:52px"><span class="on" style="left:3px">Today</span><span style="left:85px">Weekly</span><span style="left:167px">Monthly</span></div>
      <svg class="abs" style="left:0;top:0" width="279" height="308">
        <circle cx="165" cy="99" r="3" fill="#00AB8E"/><text x="174" y="102" font-size="9" fill="#333">Series 1</text>
        <circle cx="218" cy="99" r="3" fill="#FFC000"/><text x="227" y="102" font-size="9" fill="#333">Series 2</text>
        <g stroke="#f0f0f0"><line x1="46" y1="118" x2="267" y2="118"/><line x1="46" y1="149" x2="267" y2="149"/><line x1="46" y1="178" x2="267" y2="178"/><line x1="46" y1="208" x2="267" y2="208"/><line x1="46" y1="237" x2="267" y2="237"/><line x1="46" y1="266" x2="267" y2="266"/></g>
        <g font-size="10" fill="#666" text-anchor="end"><text x="40" y="122">1,000</text><text x="40" y="153">800</text><text x="40" y="182">600</text><text x="40" y="212">400</text><text x="40" y="241">200</text><text x="40" y="270">0</text></g>
        <g font-size="10" fill="#666" text-anchor="middle"><text x="66" y="284">10:00</text><text x="106" y="284">12:00</text><text x="143" y="284">1:00</text><text x="178" y="284">2:00</text><text x="213" y="284">3:00</text><text x="249" y="284">4:00</text></g>
        <polyline fill="none" stroke="#00AB8E" stroke-width="1.5" points="64,146 70,144 78,147 88,148 96,147 104,149 112,150 120,152 128,151 136,153 146,151 154,153 162,156 168,162 174,164 180,162 188,159 198,160 206,159 214,163 222,168 230,170 238,169 246,170 254,168 260,166 267,164"/>
        <polyline fill="none" stroke="#FFC000" stroke-width="1.5" points="64,170 72,169 80,172 90,173 98,174 106,176 114,175 122,177 130,177 138,180 146,183 152,180 160,181 168,182 174,186 180,188 188,189 196,188 204,187 212,187"/>
      </svg>
    </div>
    <div class="card" style="top:405px;height:300px">
      <div class="card-title" style="top:18px">Daily Walk/ Excercise</div>
      <div class="tabs" style="top:53px"><span style="left:3px">Today</span><span class="on" style="left:85px">Weekly</span><span style="left:167px">Monthly</span></div>
      <svg class="abs" style="left:0;top:0" width="279" height="300">
        <line x1="14" y1="254" x2="267" y2="254" stroke="#f0f0f0"/>
        <g fill="#e6ffd4"><rect x="24" y="134" width="11" height="119"/><rect x="61" y="111" width="11" height="142"/><rect x="135" y="128" width="11" height="125"/><rect x="172" y="158" width="11" height="95"/><rect x="209" y="116" width="11" height="137"/><rect x="246" y="134" width="11" height="119"/></g>
        <rect x="98" y="158" width="11" height="95" fill="#59FF00"/>
        <g font-size="9" fill="#777" text-anchor="middle"><text x="29" y="127">15 hr</text><text x="66" y="104">18 hr</text><text x="103" y="151">12 hr</text><text x="140" y="121">16 hr</text><text x="177" y="151">12 hr</text><text x="214" y="109">17 hr</text><text x="251" y="127">15 hr</text>
        <text x="29" y="269">Jan</text><text x="66" y="269">Mar</text><text x="103" y="269">May</text><text x="140" y="269">Jul</text><text x="177" y="269">Sep</text><text x="214" y="269">Nov</text><text x="251" y="269">Dec</text></g>
      </svg>
    </div>
  </section>

  <!-- Rehab Plan (start) -->
  <section class="phone" style="left:1196px;top:370px">
    <header class="appbar">
      <svg class="back" width="16" height="16" fill="none" stroke="#fff" stroke-width="1.6"><path d="M14 8H2M7 3L2 8l5 5"/></svg>
      <div class="title">Rehab Plan</div>
    </header>
    <div class="brand-name">Glucaro</div>
    <div class="btn">Create Rehab Plan</div>
    <div class="card" style="top:255px;height:61px">
      <p class="note abs" style="top:16px;width:100%;text-align:center">See your plan to achieve no medicine<br>diabetes control</p>
    </div>
    <div class="card" style="top:331px;height:146px">
      <p class="note abs" style="left:13px;top:15px;width:250px">See your plan to achieve no medicine diabetes control</p>
      <div class="step" style="top:56px"><b>1</b>Choose desired date</div>
      <div class="step" style="top:83px"><b>2</b>Follow sufficient diet</div>
      <div class="step" style="top:110px"><b>3</b>Enter your snacking &amp; sugar frequency</div>
    </div>
  </section>

  <!-- Daily Feed -->
  <section class="phone" style="left:548px;top:1167px">
    <header class="appbar">
      <svg class="back" width="16" height="16" fill="none" stroke="#fff" stroke-width="1.6"><path d="M14 8H2M7 3L2 8l5 5"/></svg>
      <div class="title">Daily Feed</div>
    </header>
    <div class="card" style="top:82px;height:207px">
      <div class="card-title" style="top:19px">Fasting Sugar</div>
      <svg class="abs" style="left:0;top:0" width="279" height="207">
        <defs><linearGradient id="gaugeWarm" x1="0" y1="1" x2="1" y2="0"><stop offset="0" stop-color="#F8CF3A"/><stop offset="1" stop-color="#ffa94d"/></linearGradient>
        <linearGradient id="needleUp" x1="0" y1="1" x2="0" y2="0"><stop offset="0" stop-color="#ff6a00"/><stop offset="1" stop-color="#ffb04d"/></linearGradient></defs>
        <path d="M51.4 162 A88 88 0 1 1 226.6 162" fill="none" stroke="#efefef" stroke-width="5" stroke-linecap="round"/>
        <path d="M51.4 162 A88 88 0 0 1 139 66" fill="none" stroke="url(#gaugeWarm)" stroke-width="5" stroke-linecap="round"/>
        <g stroke="#999"><line x1="59" y1="153" x2="65" y2="153"/><line x1="82" y1="96" x2="87" y2="101"/><line x1="139" y1="72" x2="139" y2="80"/><line x1="196" y1="96" x2="191" y2="101"/><line x1="219" y1="154" x2="213" y2="154"/></g>
        <g font-size="8" fill="#999" text-anchor="middle"><text x="73" y="156">1</text><text x="94" y="112">2</text><text x="139" y="91">3</text><text x="184" y="112">4</text><text x="205" y="157">5</text></g>
        <text x="55" y="190" text-anchor="middle" font-size="8" fill="#F8CF3A">Danger</text>
        <text x="224" y="190" text-anchor="middle" font-size="8" fill="#ff6b6b">Catastrophic</text>
        <polygon points="136,154 142,154 139,96" fill="url(#needleUp)"/>
        <circle cx="139" cy="154" r="7" fill="#fff" stroke="#e5e5e5"/>
        <text x="139" y="192" text-anchor="middle" font-size="14" fill="#111">5.6 <tspan font-size="6">mmol/L</tspan></text>
      </svg>
    </div>
    <div class="card" style="top:303px;height:62px">
      <svg class="abs" style="left:10px;top:16px" width="30" height="30"><circle cx="15" cy="15" r="15" fill="#E9F6FB"/><rect x="10" y="8" width="10" height="11" rx="1.5" fill="none" stroke="#00A9DD" stroke-width="1.6"/><rect x="13" y="11" width="4" height="3" fill="#00A9DD"/><line x1="15" y1="19" x2="15" y2="23" stroke="#00A9DD" stroke-width="1.6"/></svg>
      <div class="abs" style="left:53px;top:18px;font-size:11px;color:#222">Random Sugar: 56 mg/dl</div>
      <div class="abs" style="left:53px;top:34px;font-size:9px;color:#444">5:10 AM</div>
      <svg class="abs" style="left:254px;top:25px" width="10" height="14" fill="none" stroke="#00A9DD" stroke-width="1.5"><path d="M3 2l5 5-5 5"/></svg>
    </div>
    <div class="card" style="top:379px;height:297px">
      <div class="card-title" style="top:18px">Daily Walk/ Excercise</div>
      <div class="tabs" style="top:55px"><span style="left:3px">Today</span><span class="on" style="left:85px">Weekly</span><span style="left:167px">Monthly</span></div>
      <svg class="abs" style="left:0;top:0" width="279" height="297">
        <line x1="14" y1="255" x2="267" y2="255" stroke="#f0f0f0"/>
        <g fill="#e6ffd4"><rect x="25" y="134" width="11" height="120"/><rect x="61" y="111" width="11" height="143"/><rect x="135" y="129" width="11" height="125"/><rect x="172" y="157" width="11" height="97"/><rect x="209" y="117" width="11" height="137"/><rect x="246" y="134" width="11" height="120"/></g>
        <rect x="99" y="157" width="11" height="97" fill="#59FF00"/>
        <g font-size="9" fill="#777" text-anchor="middle"><text x="30" y="127">15 hr</text><text x="66" y="104">18 hr</text><text x="104" y="150">12 hr</text><text x="140" y="122">16 hr</text><text x="177" y="150">12 hr</text><text x="214" y="110">17 hr</text><text x="251" y="127">15 hr</text>
        <text x="30" y="269">Jan</text><text x="66" y="269">Mar</text><text x="104" y="269">May</text><text x="140" y="269">Jul</text><text x="177" y="269">Sep</text><text x="214" y="269">Nov</text><text x="251" y="269">Dec</text></g>
      </svg>
    </div>
  </section>

  <!-- Rehab Plan (progress) -->
  <section class="phone" style="left:980px;top:1167px">
    <header class="appbar">
      <svg class="back" width="16" height="16" fill="none" stroke="#fff" stroke-width="1.6"><path d="M14 8H2M7 3L2 8l5 5"/></svg>
      <div class="title">Rehab Plan</div>
    </header>
    <div class="card" style="top:82px;height:206px">
      <div class="card-title" style="top:16px">Total Sugar Bites</div>
      <svg class="abs" style="left:0;top:0" width="279" height="206">
        <defs><linearGradient id="donutGreen" x1="0" y1="0" x2="0" y2="1"><stop offset="0" stop-color="#59FF00"/><stop offset="1" stop-color="#82FF00"/></linearGradient></defs>
        <circle cx="139" cy="109" r="53" fill="none" stroke="#E3FFCB" stroke-width="10"/>
        <circle cx="139" cy="109" r="53" fill="none" stroke="url(#donutGreen)" stroke-width="10" stroke-dasharray="233 333" transform="rotate(-90 139 109)"/>
        <text x="139" y="114" text-anchor="middle" font-size="14" fill="#59d400">45g / 50g</text>
        <circle cx="71" cy="186" r="3" fill="#59FF00"/><text x="77" y="189" font-size="9" fill="#333">Safe</text>
        <circle cx="110" cy="186" r="3" fill="#FFC000"/><text x="116" y="189" font-size="9" fill="#333">Critical</text>
        <circle cx="162" cy="186" r="3" fill="#ff1a1a"/><text x="168" y="189" font-size="9" fill="#333">Over Limit</text>
      </svg>
    </div>
    <div class="card" style="top:302px;height:112px">
      <div class="abs" style="left:13px;top:15px;font-size:13px;color:#222">Why you want medicine-free control ?</div>
      <p class="para abs" style="left:13px;top:42px">Lorem ipsum dolor sit amet consectetur. Ut donec<br>dui ultricies dis. Nec imperdiet ultrices fusce nunc.<br>Et egestas dolor tortor ac. Risus phasellus <a>EDIT</a></p>
    </div>
    <div class="card" style="top:428px;height:260px">
      <div class="card-title" style="top:18px">Life Expectancy</div>
      <svg class="abs" style="left:0;top:0" width="279" height="260">
        <g stroke="#f0f0f0"><line x1="46" y1="69" x2="267" y2="69"/><line x1="46" y1="99" x2="267" y2="99"/><line x1="46" y1="129" x2="267" y2="129"/><line x1="46" y1="158" x2="267" y2="158"/><line x1="46" y1="187" x2="267" y2="187"/><line x1="46" y1="217" x2="267" y2="217"/></g>
        <g font-size="10" fill="#666" text-anchor="end"><text x="40" y="73">1,000</text><text x="40" y="103">800</text><text x="40" y="133">600</text><text x="40" y="162">400</text><text x="40" y="191">200</text><text x="40" y="221">0</text></g>
        <g font-size="10" fill="#666" text-anchor="middle"><text x="66" y="235">10:00</text><text x="106" y="235">12:00</text><text x="143" y="235">1:00</text><text x="178" y="235">2:00</text><text x="213" y="235">3:00</text><text x="249" y="235">4:00</text></g>
        <polyline fill="none" stroke="#00AB8E" stroke-width="1.5" points="72,155 76,150 82,150 88,147 94,146 100,142 106,142 112,138 118,135 124,130 130,127 136,127 142,129 148,128 152,122 156,118 162,116 168,111 174,109 180,104 186,103 192,104 198,100 204,98 208,96 212,93 216,90 220,85 224,82"/>
      </svg>
    </div>
  </section>
</div>
</body>
</html>
```